Upscale, Elegant Healthy Turmeric Honey Packaging Project for a Startup

We are a startup company based in North Carolina, US. We focus on benefits of Turmeric. We are looking for a packaging design that is elegant, clean looking mostly on white background which would standout on shelf as well as speak to quality of the ingredients and product.Few important points about our product1) All our ingredients are 100% USDA Organic2) Two Types of Honey - 100% Raw Unfiltered Wildflower Honey (Local). It needs to say Made by North Carolina Bees" to stand out as local honey - 100% Organic Raw Honey (non-localized)3) Our honey includes actual raw turmeric roots so this is important to communicate which is the key factor of our product4) We use Hex bottle of 12 Oz and 16 oz classic jar bottleFinal design should be clean, healthy and upscale - should be flexible to accommodate types of honey. 5 ) Back label image is attached. Our organic honey is from Brazil so Product of Brazil or Product of the USA is added to each of the back label.6) Website name needs to be in front of the label and our new website soon to be launch will be www.CrestaleMarket.com 7) We have tag line "Brovique! Bring it to your day!" which is our registered trademark needs to be included in back or front label (help us choose)We have attached some of the current simple example of our labels that we use. Provide design how it would look in the two types of bottles.

Please try to show on a bottle image of bottle (illustration) we use
https://www.vantorelsupply.com/glass-containers/cb1c-classic-glass-jar-1lb.asp for 8 oz and 16 oz
and we use
https://www.vantorelsupply.com/glass-containers/hx12c-12oz-hex-jars-w-63mm-cap.asp for 12 oz

Target Market(s)

upscale retailers, consumers, health & wealth

Colors
fcf9ce
fffbf1
fbca95
ffffff
fefdec

Requirements
Must have
• Clean, elegant look, We prefer white or off white background, Must have way to show that our honey includes raw turmeric or somehow to communicate it is turmeric honey.
Should not have
• Absolutely no similar concept of our current labels should be used in new design. Whole idea is that we are open to adopt creative ways to communicate to our customer about our product so take this as challenge.

```html
<!DOCTYPE html>
<html lang="en">
<head>
<meta charset="UTF-8">
<title>Honey with Raw Turmeric – Front Label</title>
<link rel="stylesheet" href="https://fonts.googleapis.com/css2?family=Oswald:wght@400;500;600&family=Montserrat:wght@400;600&display=swap">
<style>
  :root {
    --stage-bg: #ececec;
    --label-cream: #fffbf1;
    --root-tone: #fbca95;
    --panel-white: #ffffff;
    --panel-edge: #fbca95;
    --ink-dark: #1c1c1c;
    --turmeric-orange: #f08a1c;
    --rule-orange: #f5b46c;
    --bees-peach: #f4a865;
    --brand-green: #5ea02e;
    --brand-dot: #f08a1c;
    --body-text: #333333;
  }
  * { box-sizing: border-box; margin: 0; padding: 0; }
  html, body { width: 1200px; height: 1000px; overflow: hidden; }
  body { background: var(--stage-bg); position: relative; }

  .front-label {
    position: absolute;
    left: 290px; top: 74px;
    width: 620px; height: 852px;
    background: var(--label-cream);
    overflow: hidden;
  }
  .label-art { position: absolute; inset: 0; width: 100%; height: 100%; }

  .brand-mark {
    position: absolute;
    left: 0; top: 168px; width: 620px;
    display: flex; align-items: center; justify-content: center; gap: 12px;
  }
  .brand-mark .brand-dot {
    width: 22px; height: 22px; border-radius: 50%;
    background: var(--brand-dot);
  }
  .brand-mark .brand-name {
    font-family: 'Montserrat', sans-serif;
    font-weight: 600; font-size: 22px;
    color: var(--brand-green);
  }

  .product-title {
    position: absolute;
    left: 28px; top: 386px;
    font-family: 'Oswald', sans-serif;
    line-height: 1;
    font-weight: normal;
  }
  .product-title .title-honey {
    display: block;
    font-size: 50px; font-weight: 600;
    color: var(--ink-dark);
    letter-spacing: -0.5px;
  }
  .product-title .title-with {
    font-size: 26px; font-weight: 600;
    color: var(--ink-dark);
  }
  .product-title .title-turmeric {
    display: block;
    font-size: 56px; font-weight: 500;
    color: var(--turmeric-orange);
    margin-top: 2px;
  }

  .title-divider {
    position: absolute;
    left: 391px; top: 400px;
    width: 2px; height: 110px;
    background: var(--rule-orange);
  }

  .purity-note {
    position: absolute;
    left: 402px; top: 418px;
    width: 196px;
    font-family: 'Montserrat', sans-serif;
    font-size: 16px; line-height: 1.3;
    color: var(--body-text);
    text-align: center;
  }

  .title-rule {
    position: absolute;
    left: 28px; top: 522px;
    width: 564px; height: 3px;
    background: var(--rule-orange);
  }

  .origin-line {
    position: absolute;
    left: 0; top: 536px; width: 620px;
    text-align: center;
    font-family: 'Oswald', sans-serif;
    font-size: 29px; font-weight: 400;
    letter-spacing: 1px;
    color: var(--bees-peach);
  }

  .tagline {
    position: absolute;
    left: 0; top: 588px; width: 620px;
    text-align: center;
    font-family: 'Montserrat', sans-serif;
    font-size: 16px; font-weight: 600;
    color: var(--turmeric-orange);
  }

  .net-weight {
    position: absolute;
    left: 0; top: 648px; width: 620px;
    text-align: center;
    font-family: 'Montserrat', sans-serif;
    font-size: 17px;
    color: var(--body-text);
  }

  .website {
    position: absolute;
    left: 0; top: 678px; width: 620px;
    text-align: center;
    font-family: 'Montserrat', sans-serif;
    font-size: 14px;
    color: var(--body-text);
  }
</style>
</head>
<body>
  <section class="front-label">
    <svg class="label-art" viewBox="0 0 620 852">
      <rect width="620" height="852" fill="var(--label-cream)"/>
      <g role="img" aria-label="Faint line illustration of turmeric roots in the top right corner">
        <ellipse cx="470" cy="70" rx="170" ry="90" fill="var(--root-tone)" opacity="0.3"/>
      </g>
      <g role="img" aria-label="Faint line illustration of turmeric roots along the bottom of the label">
        <ellipse cx="300" cy="760" rx="300" ry="110" fill="var(--root-tone)" opacity="0.3"/>
      </g>
      <polygon class="label-panel" points="310,86 603,244 603,602 310,760 17,602 17,244" fill="var(--panel-white)" stroke="var(--panel-edge)" stroke-width="2"/>
    </svg>

    <div class="brand-mark">
      <span class="brand-dot"></span>
      <span class="brand-name">Sunvale Honey</span>
    </div>

    <h1 class="product-title">
      <span class="title-honey">HONEY <span class="title-with">WITH</span></span>
      <span class="title-turmeric">RAW TURMERIC</span>
    </h1>

    <div class="title-divider"></div>
    <p class="purity-note">%100 Pure Naturally Grown Raw Honey with Ancient Herb</p>

    <div class="title-rule"></div>
    <p class="origin-line">MADE BY NORTH CAROLINA BEES</p>
    <p class="tagline">Brovique! Bring it to your day!</p>

    <p class="net-weight">Net Wt. 16 oz.</p>
    <p class="website">www.CrestaleMarket.com</p>
  </section>
</body>
</html>
```